business card for a shoe shop

we would like a business card for a family owned shoe shop.
With this information included.
Darnell's Shoe Store
Family owned since 1947

then on other side
Darnell's Shoe Store
Footwear fitting specialist
Phone: 9187 2630
218 Quarry St, Fernleigh Downs 3187
(cnr. Hartwick Rd and Quarry St)
darnellshoes218@examplemail.com
if could incorporate the purple color on card i have attached.

```html
<!DOCTYPE html>
<html lang="en">
<head>
<meta charset="utf-8">
<title>Darnell's Shoe Store – Business Card</title>
<link rel="stylesheet" href="https://fonts.googleapis.com/css2?family=Ubuntu:wght@700&family=Oxygen:wght@400&display=swap">
<style>
  :root {
    --magenta: #b0137f;
    --magenta-deep: #a10a74;
    --magenta-light: #c42c9c;
    --paper: #ffffff;
    --backdrop: #dcdde0;
    --title-font: "Ubuntu", sans-serif;
    --body-font: "Oxygen", sans-serif;
  }
  * { box-sizing: border-box; margin: 0; padding: 0; }
  html, body { width: 1200px; height: 800px; overflow: hidden; }
  body {
    background: var(--backdrop);
    display: flex;
    align-items: center;
    justify-content: center;
    gap: 40px;
  }
  .card {
    width: 540px;
    height: 330px;
    position: relative;
    box-shadow: 0 6px 18px rgba(0,0,0,0.12);
  }

  /* Front */
  .card--front {
    background: linear-gradient(225deg, var(--magenta-light) 0%, var(--magenta) 50%, var(--magenta-deep) 100%);
    color: var(--paper);
    display: flex;
    flex-direction: column;
    align-items: center;
    justify-content: center;
    text-align: center;
  }
  .card--front .brand-name {
    font-family: var(--title-font);
    font-weight: 700;
    font-size: 30px;
    letter-spacing: 0.2px;
    line-height: 1.1;
  }
  .card--front .brand-tagline {
    font-family: var(--body-font);
    font-size: 17px;
    margin-top: 2px;
  }

  /* Back */
  .card--back {
    background: var(--paper);
    color: var(--magenta);
  }
  .identity {
    position: absolute;
    left: 36px;
    top: 112px;
  }
  .identity .brand-name {
    font-family: var(--title-font);
    font-weight: 700;
    font-size: 22px;
    line-height: 1.1;
  }
  .identity .brand-tagline {
    font-family: var(--body-font);
    font-size: 14px;
    margin-top: 2px;
  }
  .divider {
    position: absolute;
    left: 275px;
    top: 100px;
    width: 2px;
    height: 132px;
    background: var(--magenta);
  }
  .contacts {
    position: absolute;
    left: 294px;
    top: 132px;
    list-style: none;
    font-family: var(--body-font);
    font-size: 12px;
    line-height: 1.3;
  }
  .contact {
    display: flex;
    align-items: flex-start;
    gap: 7px;
    margin-bottom: 8px;
  }
  .contact svg { flex: none; width: 13px; height: 13px; margin-top: 1px; }
</style>
</head>
<body>
  <section class="card card--front" aria-label="Card front">
    <h1 class="brand-name">Darnell's Shoe Store</h1>
    <p class="brand-tagline">Family owned since 1947</p>
  </section>

  <section class="card card--back" aria-label="Card back">
    <div class="identity">
      <h2 class="brand-name">Darnell's Shoe Store</h2>
      <p class="brand-tagline">Footwear fitting specialist</p>
    </div>
    <div class="divider"></div>
    <ul class="contacts">
      <li class="contact">
        <svg viewBox="0 0 24 24" aria-hidden="true"><path fill="none" stroke="#b0137f" stroke-width="2.4" stroke-linejoin="round" d="M6.5 3.5l3 4-2 2.2c1.2 2.6 3.2 4.6 5.8 5.8l2.2-2 4 3-2 3.2C11 19.7 4.3 13 3.3 5.5z"/></svg>
        <span>9187 2630</span>
      </li>
      <li class="contact">
        <svg viewBox="0 0 24 24" aria-hidden="true"><circle cx="12" cy="12" r="12" fill="#b0137f"/><path fill="#fff" d="M12 5a4.5 4.5 0 0 0-4.5 4.5C7.5 13 12 18.5 12 18.5s4.5-5.5 4.5-9A4.5 4.5 0 0 0 12 5zm0 6.3a1.8 1.8 0 1 1 0-3.6 1.8 1.8 0 0 1 0 3.6z"/></svg>
        <span>218 Quarry St, Fernleigh Downs 3187<br>(cnr. Hartwick Rd and Quarry St)</span>
      </li>
      <li class="contact">
        <svg viewBox="0 0 24 24" aria-hidden="true"><rect x="2.5" y="6" width="19" height="13" rx="1" fill="none" stroke="#b0137f" stroke-width="2.4"/><path fill="none" stroke="#b0137f" stroke-width="2.4" stroke-linejoin="round" d="M2.5 7l9.5 7 9.5-7"/></svg>
        <span>darnellshoes218@examplemail.com</span>
      </li>
    </ul>
  </section>
</body>
</html>
```